I am a Life Coaching and I have purchased the logo for my business. I need business cards

I need a business card design using the logo attached (but instead of the logo saying "Harbor" I need it to say "Open Horizon Coaching"

Target Market(s)

Middle-aged people

Industry/Entity Type

Life coaching

Contact Information for Business Card

Name, email address, phone number, website

Font styles to use
Serif
Sans Serif
Script

Colors
0094D4
00A9DD
6FCCEA
C7EBF8
E9F6FB
00AB8E
00BBA5
67D7C9
C6EFE9
E9F9F6
59FF00
82FF00
B8FF75
E3FFCB
F4FFEA

Requirements
Must have
• Logo and contact info above
Nice to have
• As close to the business card inspo attached as possible

```html
<!DOCTYPE html>
<html lang="en">
<head>
<meta charset="UTF-8">
<title>Open Horizon Coaching – Business Card</title>
<link href="https://fonts.googleapis.com/css2?family=Montserrat:wght@400;500&display=swap" rel="stylesheet">
<style>
  :root {
    --backdrop: #4fb69b;
    --card-paper: #f3f3f1;
    --brand-teal: #1f9d80;
    --ink: #2b2b2b;
    --line-lime: #8be04e;
    --line-teal: #3aab88;
    --marble-light: #74dcef;
    --marble-mid: #3fc3e3;
    --marble-deep: #5c9fd8;
    --leaf-light: #e2f6cf;
    --leaf-mid: #a8e2c4;
  }
  * { margin: 0; padding: 0; box-sizing: border-box; }
  html, body {
    width: 1200px; height: 900px; overflow: hidden;
    background: var(--backdrop);
    font-family: "Montserrat", sans-serif;
  }
  .card {
    position: absolute;
    left: 401px;
    width: 413px; height: 237px;
    background: var(--card-paper);
    box-shadow: 0 6px 14px rgba(0,0,0,0.18);
    overflow: hidden;
  }
  .card--front { top: 196px; }
  .card--back { top: 477px; }

  .brand-name {
    position: absolute;
    color: var(--brand-teal);
    font-weight: 500;
    font-size: 20px;
    line-height: 1.15;
  }
  .card--front .brand-name { left: 48px; top: 50px; }
  .card--back .brand-name { left: 0; right: 0; top: 60px; text-align: center; }

  .leaf-sprig {
    position: absolute;
    left: 8px; top: 135px;
    width: 164px; height: 70px;
    border-radius: 40% 60% 30% 50%;
    background: linear-gradient(100deg, var(--leaf-light), var(--leaf-mid));
    opacity: 0.8;
  }

  .holder-name {
    position: absolute;
    left: 237px; top: 78px;
    color: var(--brand-teal);
    font-weight: 500;
    font-size: 13px;
    letter-spacing: 0.3em;
  }
  .contact-list {
    position: absolute;
    left: 222px; top: 106px;
    list-style: none;
  }
  .contact-item {
    display: flex; align-items: center;
    height: 14px;
    font-size: 7px;
    color: var(--ink);
    letter-spacing: -0.02em;
  }
  .contact-icon {
    width: 9px; height: 9px;
    margin-right: 9px;
    flex: none;
  }
  .contact-item--indent { padding-left: 18px; }

  .marble-band {
    position: absolute; left: 0; right: 0; height: 37px;
    background: linear-gradient(160deg, var(--marble-deep), var(--marble-mid) 35%, var(--marble-light) 55%, var(--marble-mid) 75%, var(--marble-deep));
  }
  .marble-band--top { top: 0; }
  .marble-band--bottom { bottom: 0; }
  .accent-line {
    position: absolute; left: 0; right: 0; height: 4px;
    background: linear-gradient(90deg, var(--line-lime), var(--line-teal));
  }
  .accent-line--top { top: 37px; }
  .accent-line--bottom { top: 196px; }
</style>
</head>
<body>
  <section class="card card--front">
    <div class="leaf-sprig" role="img" aria-label="Soft green leafy branch illustration"></div>
    <div class="brand-name">Open<br>Horizon<br>Coaching</div>

    <h1 class="holder-name">YOUR NAME</h1>
    <ul class="contact-list">
      <li class="contact-item">
        <svg class="contact-icon" viewBox="0 0 10 10" fill="none" stroke="var(--brand-teal)" stroke-width="0.9"><rect x="1" y="2.5" width="8" height="5.5"/><path d="M1 2.5 L5 5.8 L9 2.5"/></svg>
        Your@email.com
      </li>
      <li class="contact-item">
        <svg class="contact-icon" viewBox="0 0 10 10" fill="none" stroke="var(--brand-teal)" stroke-width="0.9"><path d="M2.2 1.2 L3.8 1.2 L4.4 3.2 L3.3 4 Q4.2 6 6 6.8 L6.8 5.7 L8.8 6.3 L8.8 7.9 Q8 8.9 6.5 8.6 Q2.5 7.4 1.3 3.3 Q1.1 1.9 2.2 1.2 Z"/></svg>
        +00 (123) 4567 890 (Fax)
      </li>
      <li class="contact-item contact-item--indent">+01 (715) 8521 000 (Mobile)</li>
      <li class="contact-item">
        <svg class="contact-icon" viewBox="0 0 10 10" fill="none" stroke="var(--brand-teal)" stroke-width="0.8"><circle cx="5" cy="5" r="4"/><ellipse cx="5" cy="5" rx="1.8" ry="4"/><path d="M1 5 H9 M1.6 3 H8.4 M1.6 7 H8.4"/></svg>
        www.yourweb.com
      </li>
    </ul>
  </section>

  <section class="card card--back">
    <div class="marble-band marble-band--top" role="img" aria-label="Blue and turquoise marbled paint texture"></div>
    <div class="accent-line accent-line--top"></div>
    <div class="brand-name">Open<br>Horizon<br>Coaching</div>
    <div class="accent-line accent-line--bottom"></div>
    <div class="marble-band marble-band--bottom" role="img" aria-label="Blue and turquoise marbled paint texture"></div>
  </section>
</body>
</html>
```